Brightwater Dental
Stationary for Pediatric Dental & Orthodontics - Health
Stationary for Pediatric Dental & Orthodontics
Bright & Fun-filled
Pediatrics & Orthodontics
Larkspur Hollow Prof. Center 48517 Larkspur Hollow Ave. Suite B-07 Gaithersburg, MD 20886
info@brightwaterdental.org
www.brightwaterdental.org
I have uploaded the co logo to use for the card. I am looking for biz card (2 sided), appointment card, rewards biz card (can explain later, but basically the biz card with an offer on the back), referral pad, envelope (1 sided-no flap work), letterhead, & folder. I would also like to have a QR code linked to the company website on all materials, if it can be color and still work that would be great. I uploaded the static code that I have currently.
This only needs to be on the back of the biz card not the other materials........... Helping Children Who Need: Fillings, Braces, Crowns, Laughing Gas, Whitening, Mouthguards, Hospital Care, Special Needs Care, Clearvane, Nightguards, Cosmetics, Extractions, Walk-in Emergencies, Dental Home.................... Carewell and Most Insurances Accepted

```html
<!DOCTYPE html>
<html lang="en">
<head>
<meta charset="utf-8">
<title>Brightwater Dental – Business Card</title>
<link href="https://fonts.googleapis.com/css2?family=Questrial&display=swap" rel="stylesheet">
<style>
  :root {
    --card-white: #ffffff;
    --page-bg: #e9ebee;
    --brand-blue: #1f5ba8;
    --brand-green: #7cc242;
    --text-dark: #2a2d33;
  }
  html, body {
    margin: 0;
    padding: 0;
    width: 1200px;
    height: 816px;
    overflow: hidden;
    background: var(--page-bg);
  }
  .card {
    position: relative;
    width: 1200px;
    height: 816px;
    background: var(--card-white);
    font-family: "Questrial", "Century Gothic", sans-serif;
    color: var(--text-dark);
  }
  .icon {
    position: absolute;
    width: 52px;
    height: 52px;
    border-radius: 50%;
    background: var(--brand-blue);
    display: flex;
    align-items: center;
    justify-content: center;
  }
  .icon svg { width: 28px; height: 28px; }
  .identity .icon { left: 96px; top: 212px; }
  .identity .name {
    position: absolute;
    left: 172px;
    top: 196px;
    margin: 0;
    font-size: 34px;
    font-weight: 400;
    letter-spacing: 1px;
    text-transform: uppercase;
  }
  .identity .role {
    position: absolute;
    left: 172px;
    top: 238px;
    margin: 0;
    font-size: 30px;
    letter-spacing: 1px;
  }
  .accent-rule {
    position: absolute;
    left: 0;
    top: 306px;
    width: 560px;
    height: 5px;
    background: var(--brand-green);
  }
  .contact-row { position: absolute; left: 96px; }
  .contact-row .icon { position: absolute; left: 0; top: 0; }
  .contact-row p {
    position: absolute;
    left: 76px;
    margin: 0;
    font-size: 27px;
    line-height: 32px;
    white-space: nowrap;
  }
  .row-phone { top: 400px; }
  .row-phone p { top: -28px; }
  .row-web { top: 510px; }
  .row-web p { top: -22px; }
  .row-address { top: 620px; }
  .row-address p { top: -22px; }
  .brand {
    position: absolute;
    left: 640px;
    top: 420px;
    display: flex;
    align-items: center;
    gap: 16px;
  }
  .brand-dot {
    width: 62px;
    height: 62px;
    border-radius: 50%;
    background: var(--brand-blue);
  }
  .brand-name {
    margin: 0;
    font-size: 52px;
    color: var(--brand-blue);
    letter-spacing: 1px;
  }
  .brand-tagline {
    position: absolute;
    left: 718px;
    top: 494px;
    margin: 0;
    font-size: 24px;
    color: var(--brand-green);
    letter-spacing: 1px;
  }
</style>
</head>
<body>
<main class="card">
  <section class="identity">
    <span class="icon">
      <svg viewBox="0 0 24 24" fill="#fff"><circle cx="12" cy="8" r="4.5"/><path d="M3 22c0-5 4-8 9-8s9 3 9 8z"/></svg>
    </span>
    <h1 class="name">Marcus Holloway</h1>
    <p class="role">Managing Director</p>
  </section>

  <div class="accent-rule"></div>

  <div class="contact-row row-phone">
    <span class="icon">
      <svg viewBox="0 0 24 24" fill="none" stroke="#fff" stroke-width="2"><rect x="7" y="2" width="10" height="20" rx="2"/><line x1="11" y1="18" x2="13" y2="18"/></svg>
    </span>
    <p>014 382 5907<br>014 382 5907</p>
  </div>

  <div class="contact-row row-web">
    <span class="icon">
      <svg viewBox="0 0 24 24" fill="none" stroke="#fff" stroke-width="2"><rect x="3" y="4" width="18" height="12" rx="1"/><line x1="12" y1="16" x2="12" y2="20"/><line x1="8" y1="20" x2="16" y2="20"/></svg>
    </span>
    <p>yourname@mailbox.com<br>yourwebsite.com</p>
  </div>

  <div class="contact-row row-address">
    <span class="icon">
      <svg viewBox="0 0 24 24" fill="#fff"><path d="M12 2a7 7 0 0 0-7 7c0 5 7 13 7 13s7-8 7-13a7 7 0 0 0-7-7zm0 9.5a2.5 2.5 0 1 1 0-5 2.5 2.5 0 0 1 0 5z"/></svg>
    </span>
    <p>217 9th Floor, Crest<br>Landmark Road MRK</p>
  </div>

  <div class="brand">
    <span class="brand-dot"></span>
    <p class="brand-name">Brightwater Dental</p>
  </div>
  <p class="brand-tagline">Pediatrics &amp; Orthodontics</p>
</main>
</body>
</html>
```